New Corporate website more focused on funnel and great design

Our company, Bold Harbor needs a new website to look like it's from 2021. We work with large businesses in the corporte world and need to reflect that we are professional, focused on our clients, and trsutworthy. It should include some/most of the components from our current site: boldharbor.com but should focus more about getting people to optin to out free downloads, which can be found on this page: https://www.boldharbor.com/get-started-with-a-prep-session/ and this page: https://www.boldharbor.com/team-onboarding/

Our new website should do a better job at explaining what we do, who we serve, and how we fix their problems of onboarding new leaders. Feel free to use dummy text if you are not sure what to put in for certain sections. I also would like to point out that most of the audiance is older, so we don't need anything too younge and flashy, or that is hard it use. it should have big clear fonts, plently of contrast, and work well for poeple who are not good at using the internet. Please use the colors of the logo, and you can add another color or two if you think it's fits

Industry/Entity Type

business consulting

Number of Pages Required

2 page

Font styles to use
Sans Serif

Requirements
Must have
• corporate feel, look professional, focus on getting new leads
Should not have
• cute or children feel

```html
<!DOCTYPE html>
<html lang="en">
<head>
<meta charset="utf-8">
<title>Bold Harbor – Website Presentation</title>
<link href="https://fonts.googleapis.com/css2?family=Lato:wght@400;700;900&display=swap" rel="stylesheet">
<style>
:root{
  --board:#b7d4ea;
  --navy:#164b8b;
  --navy-dark:#0f3a6e;
  --navy-soft:#2b609f;
  --light:#e8edf3;
  --ink:#26313d;
  --muted:#6b7683;
  --white:#ffffff;
  --footer:#232427;
  --photo-a:#5b6877;
  --photo-b:#243140;
}
*{box-sizing:border-box;margin:0;padding:0}
html,body{width:1200px;height:3750px;overflow:hidden}
body{background:var(--board);font-family:'Lato',sans-serif;color:var(--ink);position:relative}
.abs{position:absolute}
.brand{display:flex;align-items:center;gap:6px;font-weight:700;color:var(--navy);white-space:nowrap}
.brand-mark{background:var(--navy);display:inline-block}
.photo{background:linear-gradient(135deg,var(--photo-a),var(--photo-b))}
.photo-light{background:linear-gradient(135deg,#c9d2dc,#7f8d9c)}
.btn{display:inline-block;background:var(--navy);color:var(--white);font-weight:700;text-transform:uppercase;letter-spacing:.3px}
.btn-white{background:var(--white);color:var(--navy)}
.side-label{position:absolute;font-size:18px;letter-spacing:12px;color:var(--navy);transform:rotate(-90deg);transform-origin:left top;white-space:nowrap}

/* ---------- top showcase ---------- */
.board-logo{left:495px;top:122px}
.board-logo .brand{font-size:28px;gap:10px}
.board-logo .brand-mark{width:30px;height:30px}

.screen-laptop{left:256px;top:277px;width:731px;height:469px;background:var(--white);overflow:hidden}
.sl-top{height:18px;background:var(--navy);display:flex;align-items:center;padding-left:100px;gap:24px;font-size:8px;color:var(--white)}
.sl-top .quote{margin-left:auto;background:var(--navy-dark);height:18px;line-height:18px;padding:0 18px 0 16px;font-weight:700;margin-right:98px}
.sl-nav{height:52px;display:flex;align-items:center;padding:0 100px 0 98px}
.sl-nav .brand{font-size:15px}.sl-nav .brand-mark{width:16px;height:16px}
.sl-nav ul{margin-left:auto;display:flex;gap:16px;list-style:none;font-size:8px}
.sl-nav li.on{color:var(--navy);text-decoration:underline}
.sl-hero{height:399px;position:relative}
.sl-hero h1{position:absolute;left:99px;top:95px;color:var(--white);font-size:25px;line-height:32px;font-weight:700}
.sl-hero p{position:absolute;left:99px;top:170px;color:var(--white);font-size:8px;line-height:13px;width:400px;font-style:italic}
.sl-hero .btns{position:absolute;left:99px;top:215px;display:flex;gap:8px}
.sl-hero .btn{font-size:7px;padding:10px 10px}

.screen-phone{left:138px;top:463px;width:162px;height:312px;background:var(--white);overflow:hidden;border:3px solid #1c1f24;border-radius:10px}
.sp-top{height:12px;background:var(--navy);font-size:4px;color:var(--white);display:flex;align-items:center;gap:6px;padding-left:6px}
.sp-nav{height:34px;display:flex;align-items:center;justify-content:space-between;padding:0 8px}
.sp-nav .brand{font-size:8px;gap:3px}.sp-nav .brand-mark{width:9px;height:9px}
.burger{width:10px;height:7px;border-top:1.5px solid var(--ink);border-bottom:1.5px solid var(--ink);position:relative}
.burger:after{content:"";position:absolute;left:0;right:0;top:1.3px;border-top:1.5px solid var(--ink)}
.sp-hero{height:260px;position:relative}
.sp-hero h1{position:absolute;left:12px;top:70px;color:var(--white);font-size:11px;line-height:14px;font-weight:700;width:140px}
.sp-hero p{position:absolute;left:12px;top:118px;color:var(--white);font-size:5px;line-height:7px;width:135px}
.sp-hero .btns{position:absolute;left:12px;top:150px;display:flex;gap:6px}
.sp-hero .btn{font-size:4.5px;padding:7px 8px}

/* ---------- desktop page ---------- */
.desk{left:419px;top:849px;width:554px;height:2777px;background:var(--white);overflow:hidden;font-size:5px;line-height:8px}
.desk section{position:relative;overflow:hidden}
.eyebrow{font-size:4.5px;letter-spacing:1px;text-transform:uppercase;color:var(--muted)}
.h2{font-size:13px;line-height:16px;font-weight:700;color:var(--ink)}
.d-top{height:17px;background:var(--navy);color:var(--white);display:flex;align-items:center;font-size:4.5px;padding-left:76px;gap:16px}
.d-top .quote{margin-left:auto;margin-right:75px;background:var(--navy-dark);height:17px;line-height:17px;padding:0 12px;font-weight:700}
.d-nav{height:41px;display:flex;align-items:center;padding:0 75px}
.d-nav .brand{font-size:11px;gap:5px}.d-nav .brand-mark{width:12px;height:12px}
.d-nav ul{margin-left:auto;display:flex;gap:10px;list-style:none;font-size:5px}
.d-nav li.on{color:var(--navy);text-decoration:underline}
.d-hero{height:341px}
.d-hero h1{position:absolute;left:75px;top:105px;color:var(--white);font-size:18px;line-height:24px;font-weight:700}
.d-hero p{position:absolute;left:75px;top:160px;color:var(--white);font-size:5px;line-height:8px;width:300px;font-style:italic}
.d-hero .btns{position:absolute;left:75px;top:192px;display:flex;gap:6px}
.d-hero .btn{font-size:5px;padding:7px 7px}
.d-welcome{height:95px;background:var(--light)}
.d-welcome .h2{position:absolute;left:75px;top:32px;color:var(--navy)}
.d-welcome .h2 span{color:var(--ink)}
.d-welcome p{position:absolute;left:197px;top:34px;width:160px;font-size:4.5px;line-height:8px;color:var(--muted)}
.d-welcome .btn{position:absolute;left:387px;top:36px;font-size:4.5px;padding:7px 11px}
.d-who{height:245px}
.d-who .txt{position:absolute;left:75px;top:30px;width:200px}
.d-who .txt p{font-size:4.5px;line-height:8px;color:var(--muted);margin-top:6px}
.ticks{display:grid;grid-template-columns:repeat(3,auto);gap:3px 8px;margin-top:8px;font-size:4.5px;color:var(--muted)}
.ticks span:before{content:"✓ ";color:var(--navy)}
.d-who .btn{font-size:4.5px;padding:7px 12px;margin-top:12px}
.d-who .pic{position:absolute;left:318px;top:33px;width:160px;height:179px}
.badge{position:absolute;right:0;bottom:38px;width:62px;height:50px;background:var(--white);text-align:center;padding-top:10px}
.badge b{font-size:15px;color:var(--navy);display:block;line-height:16px}
.badge span{font-size:4px;color:var(--muted)}
.d-what{height:284px;background:var(--navy);color:var(--white);text-align:center}
.d-what .eyebrow,.d-case .eyebrow{color:#b9cbe2}
.d-what .h2{color:var(--white);margin-top:2px}
.d-what .lead{width:300px;margin:6px auto 0;font-size:4.5px;line-height:8px;color:#d6e1ef}
.cards{position:absolute;left:75px;top:102px;display:flex;gap:10px}
.card{width:128px;height:124px;background:var(--navy-soft)}
.card .pic{height:74px}
.card b{display:block;font-size:5px;letter-spacing:.6px;margin-top:12px;text-transform:uppercase}
.card small{display:block;font-size:4px;margin-top:6px;color:#d6e1ef}
.card.on{background:var(--white);color:var(--navy)}.card.on small{color:var(--navy)}
.d-what .note{position:absolute;left:0;right:0;top:250px;font-size:4.5px;color:#d6e1ef}
.d-what .note u{color:var(--white);font-weight:700}
.d-help{height:291px;background:var(--light)}
.d-help .pic{position:absolute;left:0;top:0;width:251px;height:291px}
.d-help .txt{position:absolute;left:265px;top:34px;width:215px}
.d-help p{font-size:4.5px;line-height:8px;color:var(--muted);margin-top:6px}
.feat{display:grid;grid-template-columns:1fr 1fr;gap:8px 10px;margin-top:10px}
.feat div{display:flex;align-items:center;gap:6px;font-size:4.5px}
.feat i{width:15px;height:15px;border-radius:50%;background:var(--navy);opacity:.8;flex:none}
.feat span{flex:1;background:#d8e0ea;padding:5px 0;text-align:center}
.d-help .btn{font-size:4.5px;padding:7px 12px;margin-top:14px}
.d-test{height:294px;text-align:center;background:radial-gradient(ellipse at center,#eef1f5 0%,#fff 70%)}
.d-test .top{margin-top:30px}
.quotes{position:absolute;left:75px;top:82px;display:flex;gap:10px}
.quote-card{width:197px}
.quote-card .box{height:83px;background:var(--navy);color:var(--white);font-size:4.5px;line-height:8px;font-style:italic;padding:14px 18px 0}
.quote-card .box b{display:block;font-size:12px;font-style:normal;line-height:10px}
.quote-card .who{font-size:4.5px;margin-top:8px;font-weight:700}
.quote-card .role{font-size:4px;color:var(--muted)}
.dots{position:absolute;left:0;right:0;top:254px;display:flex;justify-content:center;gap:4px}
.dots i{width:4px;height:4px;border-radius:50%;background:#c6d1de}.dots i.on{background:var(--navy)}
.d-case{height:216px;background:var(--navy);color:var(--white)}
.d-case .pic{position:absolute;right:0;top:0;width:245px;height:216px}
.d-case .txt{position:absolute;left:75px;top:30px;width:200px}
.d-case .h2{color:var(--white);margin-bottom:10px}
.d-case li{list-style:none;font-size:4.5px;display:flex;justify-content:space-between;padding:5px 0}
.d-books{height:331px;text-align:center}
.d-books .top{margin-top:28px}
.posts{position:absolute;left:75px;top:88px;display:flex;gap:10px;text-align:left}
.post{width:128px}
.post .pic{height:86px;position:relative}
.post .tag{position:absolute;right:4px;top:6px;background:var(--navy);color:var(--white);font-size:3.5px;padding:1px 4px}
.post h4{font-size:5px;line-height:8px;margin-top:6px}
.post p{font-size:4px;line-height:7px;color:var(--muted);margin-top:4px}
.post .more{text-align:right;font-size:4px;color:var(--navy);margin-top:6px}
.book{width:128px;height:130px;border:1px solid #d8dee6;display:flex;flex-direction:column;align-items:center;justify-content:center;gap:8px}
.book .cover{width:68px;height:88px;background:linear-gradient(#f3f0ea,#d9d3c7);border:1px solid #bcb5a8}
.book small{font-size:4px;color:var(--navy)}
.d-books .btn{position:absolute;left:246px;top:258px;font-size:4.5px;padding:7px 10px}
.d-contact{height:390px;background:var(--light)}
.d-contact .band{position:absolute;left:0;top:0;width:100%;height:172px}
.d-contact h3{position:absolute;left:0;right:0;top:52px;text-align:center;color:var(--white);font-size:13px;line-height:16px}
.d-contact .eyebrow{position:absolute;left:0;right:0;top:44px;text-align:center;color:#c9d1da}
.form{position:absolute;left:75px;top:148px;width:404px;height:173px;background:var(--white);padding:28px 24px 0;text-align:center}
.form .brand{justify-content:center;font-size:10px}.form .brand-mark{width:11px;height:11px}
.fields{display:grid;grid-template-columns:1fr 1fr;gap:8px 14px;margin-top:18px;text-align:left}
.fields span{border:1px solid #dfe4ea;font-size:4.5px;padding:5px 8px;color:var(--muted)}
.form .btn{font-size:4.5px;padding:7px 10px;margin-top:18px}
.partners{position:absolute;left:75px;top:338px;width:404px;display:flex;gap:12px}
.partners span{flex:1;height:28px;background:var(--white);display:flex;align-items:center;justify-content:center;font-size:8px;font-weight:700;color:var(--ink)}
.d-contact .more{position:absolute;left:0;right:0;top:376px;text-align:center;font-size:4px;color:var(--navy);text-decoration:underline}
.d-foot{height:214px;background:var(--footer);color:#cfd3d8}
.d-foot .col{position:absolute;top:40px}
.d-foot .brand{color:var(--white);font-size:10px}.d-foot .brand-mark{width:11px;height:11px;background:var(--white)}
.d-foot h5{color:var(--white);font-size:8px;font-weight:700}
.d-foot p,.d-foot li{font-size:4.5px;line-height:10px;list-style:none}
.soc{display:flex;gap:5px;margin-top:12px}.soc i{width:11px;height:11px;background:var(--white)}
.d-copy{height:18px;background:var(--navy);color:var(--white);font-size:4px;text-align:center;line-height:18px}

/* ---------- mobile page ---------- */
.mob{left:237px;top:849px;width:108px;height:2777px;background:var(--white);overflow:hidden;font-size:3px;line-height:5px}
.mob section{position:relative;overflow:hidden}
.mob .pad{padding:0 7px}
.mob .h{font-size:6.5px;line-height:8px;font-weight:700}
.mob .e{font-size:2.8px;letter-spacing:.5px;color:var(--muted);text-transform:uppercase}
.mob p{color:var(--muted)}
.mob .btn{font-size:2.8px;padding:3px 6px}
.m-top{height:8px;background:var(--navy)}
.m-nav{height:27px;display:flex;align-items:center;justify-content:space-between;padding:0 7px}
.m-nav .brand{font-size:5.5px;gap:2px}.m-nav .brand-mark{width:6px;height:6px}
.m-nav .burger{width:7px;height:5px;border-width:1px}
.m-hero{height:165px}
.m-hero .h{position:absolute;left:7px;top:42px;color:var(--white);width:95px;font-size:6px;line-height:7.5px}
.m-hero .btns{position:absolute;left:7px;top:93px;display:flex;gap:4px}
.m-welcome{height:95px;background:var(--light);padding-top:22px}
.m-welcome .h{color:var(--navy)}
.m-who{height:284px;padding-top:30px}
.m-who .pic{height:86px;margin:0 7px 14px}
.m-what{height:374px;background:var(--navy);color:var(--white);padding-top:18px}
.m-what p{color:#d6e1ef}
.m-card{margin:6px 7px 0;height:86px;background:var(--navy-soft);text-align:center}
.m-card .pic{height:54px}.m-card b{display:block;font-size:3px;margin-top:8px}
.m-card.on{background:var(--white);color:var(--navy)}
.m-help{height:361px;background:var(--light)}
.m-help .pic{height:106px;margin-bottom:20px}
.m-feat{margin-top:6px;display:flex;flex-direction:column;gap:4px}
.m-feat div{display:flex;gap:4px;align-items:center}.m-feat i{width:9px;height:9px;border-radius:50%;background:var(--navy);opacity:.8}
.m-feat span{flex:1;background:#d8e0ea;height:9px}
.m-test{height:207px;padding-top:14px}
.m-test .box{margin:8px 7px 0;height:100px;background:var(--navy);color:#d6e1ef;padding:10px 8px;text-align:center;font-style:italic}
.m-case{height:252px;background:var(--white)}
.m-case .pic{height:100px;margin-bottom:16px}
.m-case li{list-style:none;display:flex;justify-content:space-between;padding:3px 0;border-bottom:1px solid #eef1f4}
.m-books{height:462px;padding-top:12px}
.m-books .book{width:94px;height:102px;margin:8px 7px 0}
.m-books .book .cover{width:48px;height:62px}
.m-post{margin:10px 7px 0}.m-post .pic{height:56px}
.m-contact{height:280px;background:var(--light)}
.m-contact .band{height:92px;padding:14px 7px 0}
.m-contact .band .h{color:var(--white)}
.m-form{margin:-14px 7px 0;background:var(--white);height:120px;padding:10px 8px;position:relative}
.m-form .brand{justify-content:center;font-size:5px}.m-form .brand-mark{width:5px;height:5px}
.m-form span{display:block;border:1px solid #dfe4ea;height:8px;margin-top:5px}
.m-partner{margin:14px 7px 0;height:18px;background:var(--white);display:flex;align-items:center;justify-content:center;font-size:5px;font-weight:700}
.m-foot{height:248px;background:var(--footer);color:#cfd3d8;padding:14px 7px}
.m-foot .brand{color:var(--white);font-size:5.5px}.m-foot .brand-mark{width:6px;height:6px;background:var(--white)}
.m-foot b{display:block;color:var(--white);font-size:4.5px;margin-top:14px}
.m-copy{height:14px;background:var(--navy);color:var(--white);font-size:2.5px;text-align:center;line-height:14px}
</style>
</head>
<body>

<div class="abs board-logo"><div class="brand"><i class="brand-mark"></i>Bold Harbor</div></div>

<div class="abs screen-laptop">
  <div class="sl-top"><span>☎ +1 555.010.4400</span><span>✉ boldharbor@email.com</span><span class="quote">FREE QUOTE</span></div>
  <div class="sl-nav"><div class="brand"><i class="brand-mark"></i>Bold Harbor</div>
    <ul><li class="on">Home</li><li>Who We Are</li><li>What We Do</li><li>Clients</li><li>Blog</li><li>Resources</li><li>Contact</li></ul></div>
  <div class="sl-hero photo" role="img" aria-label="Photo of executives in a boardroom meeting">
    <h1>Accelerate Business Performance<br>During Critical Leadership Transitions</h1>
    <p>Lorem ipsum dolor sit amet, consectetur adipiscing elit, sed do eiusmod tempor incididunt ut labore et dolore magna aliqua. Quis ipsum suspendisse ultrices gravida. Risus commodo viverra maecenas accumsan lacus vel facilisis.</p>
    <div class="btns"><span class="btn btn-white">Free Download</span><span class="btn">Contact Us</span></div>
  </div>
</div>

<div class="abs screen-phone">
  <div class="sp-top"><span>+1 555.010.4400</span><span>boldharbor@email.com</span></div>
  <div class="sp-nav"><div class="brand"><i class="brand-mark"></i>Bold Harbor</div><span class="burger"></span></div>
  <div class="sp-hero photo" role="img" aria-label="Photo of an executive leading a boardroom meeting">
    <h1>Accelerate Business Performance During Critical Leadership Transitions</h1>
    <p>Lorem ipsum dolor sit amet, consectetur adipiscing elit, sed do eiusmod tempor incididunt ut labore dolore.</p>
    <div class="btns"><span class="btn btn-white">Free Download</span><span class="btn">Contact Us</span></div>
  </div>
</div>

<div class="side-label" style="left:176px;top:2210px">RESPONSIVE SIDE</div>
<div class="side-label" style="left:990px;top:2425px">LAPTOP / DESKTOP</div>

<div class="abs mob">
  <div class="m-top"></div>
  <div class="m-nav"><div class="brand"><i class="brand-mark"></i>Bold Harbor</div><span class="burger"></span></div>
  <section class="m-hero photo" role="img" aria-label="Photo of executives in a meeting">
    <div class="h">Accelerate Business Performance During Critical Leadership Transitions</div>
    <div class="btns"><span class="btn btn-white">Free Download</span><span class="btn">Contact Us</span></div>
  </section>
  <section class="m-welcome pad"><div class="h"><span style="color:var(--ink)">Welcome To</span><br>Bold Harbor</div>
    <p style="margin:5px 0">Looking for a first class business plan consulting partner? Get done in 100 days what normally takes 6–12 months for most clients.</p>
    <span class="btn">Start With Prep Session</span></section>
  <section class="m-who">
    <div class="pic photo-light" role="img" aria-label="Photo of business people shaking hands"></div>
    <div class="pad"><div class="e">About Us</div><div class="h">Who We Are</div>
    <p style="margin-top:4px">Bold Harbor accelerates the leaders and teams to deliver better results faster through critical transitions, leading to short term and lasting success for the leader and the organization.</p>
    <p style="margin-top:4px">✓ Lorem ipsum dolor ✓ Dolor ipsum lorem ✓ Dolor lorem ipsum</p>
    <p style="margin-top:4px">Since 2003, across hundreds of client engagements in numerous industries and markets, we have helped leaders and teams in critical circumstances.</p></div>
  </section>
  <section class="m-what">
    <div class="pad"><div class="e" style="color:#b9cbe2">Services</div><div class="h">What We Do</div><p>Some text filler for design purposes, lorem ipsum dolor sit amet.</p></div>
    <div class="m-card"><div class="pic photo-light" role="img" aria-label="Photo of a leader at a desk"></div><b>EXECUTIVE ON-BOARDING</b></div>
    <div class="m-card on"><div class="pic photo-light" role="img" aria-label="Photo of a team meeting"></div><b>TEAM ON-BOARDING</b></div>
    <div class="m-card"><div class="pic photo-light" role="img" aria-label="Photo of colleagues at a table"></div><b>ACCELERATION &amp; RESTART</b></div>
    <p class="pad" style="margin-top:8px">We provide two ways to manage your business. Request your quote here →</p>
  </section>
  <section class="m-help">
    <div class="pic photo" role="img" aria-label="Photo of a smiling executive in glasses"></div>
    <div class="pad"><div class="e">Business Solutions</div><div class="h">How We Help You?</div>
    <p style="margin-top:4px">Our team tools and unique perspective are developed with practicality, flexibility and client success in mind.</p>
    <div class="m-feat"><div><i></i><span></span></div><div><i></i><span></span></div><div><i></i><span></span></div><div><i></i><span></span></div></div>
    <p style="margin:6px 0">Our tools are built and adapted from best practices and real life experiences.</p><span class="btn">Get Started</span></div>
  </section>
  <section class="m-test"><div class="pad"><div class="e">What Our Clients Say</div><div class="h">Testimonials</div></div>
    <div class="box"><b style="font-size:7px;font-style:normal">”</b><br>You helped us simplify the complex, interpret our complexity and articulate our mission, vision and strategies.</div>
    <p style="text-align:center;margin-top:5px;color:var(--ink)">Laura Kemp</p></section>
  <section class="m-case"><div class="pic photo" role="img" aria-label="Photo of a busy open-plan office"></div>
    <div class="pad"><div class="e">Some text filler here</div><div class="h">Case Studies</div>
    <ul style="margin-top:4px"><li>Private Equity CEO Accelerates Exit<span>→</span></li><li>New CEO Accelerates Team Results<span>→</span></li><li>New CEO Leads Successful Exit<span>→</span></li><li>Private Equity CEO Merger Plan<span>→</span></li><li>New Medical Center CEO Change<span>→</span></li><li>SVP Global Operations Drives Results<span>→</span></li></ul></div></section>
  <section class="m-books"><div class="pad"><div class="e">Featured Books and News</div><div class="h">Books &amp; Blog Posts</div></div>
    <div class="book"><div class="cover" role="img" aria-label="Book cover of The First Quarter Playbook"></div><small>Browse All Of Our Books →</small></div>
    <div class="m-post"><div class="pic photo-light" role="img" aria-label="Photo of a framed portrait"></div><p style="color:var(--ink);margin-top:3px">When To Inform In Advance Versus Report After The Fact</p></div>
    <div class="m-post"><div class="pic photo" role="img" aria-label="Photo of executives at a conference"></div><p style="color:var(--ink);margin-top:3px">Why Halvern's New CFO Should Fail, But Won't</p></div>
    <div class="pad" style="margin-top:10px"><span class="btn">Read All Posts</span></div></section>
  <section class="m-contact"><div class="band photo" role="img" aria-label="Dark photo of a meeting room"><div class="h">Got Any Project You Would Like To Discuss? Please Fill The Form Below:</div></div>
    <div class="m-form"><div class="brand"><i class="brand-mark"></i>Bold Harbor</div><span></span><span></span><span></span><span></span><div style="margin-top:8px"><span class="btn" style="display:inline-block;border:0;height:auto">Send Message</span></div></div>
    <div class="m-partner">Northvale</div></section>
  <section class="m-foot"><div class="brand"><i class="brand-mark"></i>Bold Harbor</div>
    <p style="color:#cfd3d8;margin-top:5px">Get done in 100 days what normally takes 6–12 months for our clients.</p>
    <div class="soc"><i style="width:6px;height:6px"></i><i style="width:6px;height:6px"></i><i style="width:6px;height:6px"></i></div>
    <b>Quick Links</b><p style="color:#cfd3d8">Home<br>About Us<br>Books<br>Events<br>Resources</p>
    <b>Contact Us</b><p style="color:#cfd3d8">☎ +1 555.010.4400<br>✉ boldharbor@email.com<br>⌖ Lorem Ipsum Street, USA</p></section>
  <div class="m-copy">Copyright © 2021 Bold Harbor – All Rights Reserved</div>
</div>

<div class="abs desk">
  <div class="d-top"><span>☎ +1 555.010.4400</span><span>✉ boldharbor@email.com</span><span class="quote">FREE QUOTE</span></div>
  <div class="d-nav"><div class="brand"><i class="brand-mark"></i>Bold Harbor</div>
    <ul><li class="on">Home</li><li>Who We Are</li><li>What We Do</li><li>Clients</li><li>Blog</li><li>Resources</li><li>Contact</li></ul></div>

  <section class="d-hero photo" role="img" aria-label="Photo of executives in a boardroom meeting">
    <h1>Accelerate Business Performance<br>During Critical Leadership Transitions</h1>
    <p>Lorem ipsum dolor sit amet, consectetur adipiscing elit, sed do eiusmod tempor incididunt ut labore et dolore magna aliqua. Quis ipsum suspendisse ultrices gravida. Risus commodo viverra maecenas accumsan lacus vel facilisis.</p>
    <div class="btns"><span class="btn btn-white">Free Download</span><span class="btn">Contact Us</span></div>
  </section>

  <section class="d-welcome">
    <div class="h2"><span>Welcome To</span><br>Bold Harbor</div>
    <p>Looking for a First Class Business Plan Consulting Corporate? Get done in 100 days what normally takes 6–12 months 95% of Bold Harbor clients succeed.</p>
    <span class="btn">Start With Prep Session</span>
  </section>

  <section class="d-who">
    <div class="txt"><div class="eyebrow">About Us</div><div class="h2">Who We Are</div>
      <p>Bold Harbor accelerates the leaders and teams to deliver better results faster through critical transitions, leading to short term and lasting success for the leader and the organization.</p>
      <div class="ticks"><span>Lorem ipsum Dolor</span><span>Dolor ipsum lorem</span><span>Dolor Lorem ipsum</span><span>Lorem Dolor ipsum</span><span>Ipsum Lorem Dolor</span><span>Ipsum Dolor lorem</span></div>
      <p>Since 2003, across hundreds of client engagements in numerous industries and markets around the world, we've helped leaders and teams in the most challenging circumstances. Learn more about our support across Executive Onboarding, Team Onboarding and Acceleration &amp; Restart transitions.</p>
      <span class="btn">Learn More</span></div>
    <div class="pic photo-light" role="img" aria-label="Photo of business people shaking hands in an office">
      <div class="badge"><b>2003</b><span>ESTABLISHED</span></div></div>
  </section>

  <section class="d-what">
    <div style="padding-top:32px"><div class="eyebrow">Services</div><div class="h2">What We Do</div>
    <p class="lead">Some text filler for design purposes. Lorem ipsum dolor sit amet, consectetur adipiscing elit, sed do eiusmod tempor incididunt ut labore et dolore magna aliqua.</p></div>
    <div class="cards">
      <div class="card"><div class="pic photo-light" role="img" aria-label="Photo of a leader reviewing documents"></div><b>Executive On-Boarding</b><small>Read More →</small></div>
      <div class="card on"><div class="pic photo-light" role="img" aria-label="Photo of a team in discussion"></div><b>Team On-Boarding</b><small>Read More →</small></div>
      <div class="card"><div class="pic photo-light" role="img" aria-label="Photo of colleagues around a laptop"></div><b>Acceleration &amp; Restart</b><small>Read More →</small></div>
    </div>
    <div class="note">We provide two ways to manage your businesses. <u>Request your Quote here</u> →</div>
  </section>

  <section class="d-help">
    <div class="pic photo" role="img" aria-label="Photo of a smiling executive in glasses gesturing"></div>
    <div class="txt"><div class="eyebrow">Business Solutions</div><div class="h2">How We Help You?</div>
      <p>Our team tools and unique perspective are developed with practicality, flexibility and client success in mind.</p>
      <p>Our team comprises of former CEOs, presidents, managing directors, and organizational development experts who've been in your shoes, planned and survived.</p>
      <div class="feat"><div><i></i><span>Experienced Team</span></div><div><i></i><span>Beyond Advisory</span></div><div><i></i><span>Lorem Ipsum Dolor</span></div><div><i></i><span>Some Text Filler</span></div></div>
      <p>Our tools are built and adapted from best practices and real life experiences with our clients. We are not wedded to our tools: we use what works.</p>
      <span class="btn">Get Started</span></div>
  </section>

  <section class="d-test">
    <div class="top"><div class="eyebrow">What Our Clients Say</div><div class="h2">Testimonials</div></div>
    <div class="quotes">
      <div class="quote-card"><div class="box"><b>”</b>“You helped us simplify the complex, interpret our complexity and articulate our mission, vision and strategies. You helped build our confidence, showed us that we do know what we need to do to grow our business.”</div>
        <div class="who">Laura Kemp</div><div class="role">President, Supply Services, Corvane Health</div></div>
      <div class="quote-card"><div class="box"><b>”</b>“You were an incredibly useful sounding board, speaking with experience and authority. The tools and partners are practical and hands-on, helping us get the job done. We have completely turned around the motivation of this team.”</div>
        <div class="who">Dan Mercer</div><div class="role">SVP-GTM, Harwell Systems</div></div>
    </div>
    <div class="dots"><i></i><i class="on"></i><i></i></div>
  </section>

  <section class="d-case">
    <div class="txt"><div class="eyebrow">Some Text Filler Here</div><div class="h2">Case Studies</div>
      <ul><li>Private Equity CEO Accelerates Exit<span>→</span></li><li>New CEO Leads Successful Private Equity Exit<span>→</span></li><li>New CEO Accelerates Team and Share Performance<span>→</span></li><li>Private Equity CEO Accelerates Merger of Five Businesses<span>→</span></li><li>New Medical Center CEO Drives Culture Change and Results<span>→</span></li><li>SVP Global Operations Drives Change and Results, Gets Promoted<span>→</span></li></ul></div>
    <div class="pic photo" role="img" aria-label="Photo of a busy open-plan office"></div>
  </section>

  <section class="d-books">
    <div class="top"><div class="eyebrow">Featured Books and News</div><div class="h2">Books &amp; Blog Posts</div></div>
    <div class="posts">
      <div class="post"><div class="pic photo-light" role="img" aria-label="Photo of a framed portrait on a wall"><span class="tag">Onboarding</span></div>
        <h4>When To Inform In Advance Versus Report After The Fact</h4><p>By Martin Hale | On Jul 20, 2021</p><p>The critical difference between "inform" and "report" is timing. Informing happens before and reporting...</p><div class="more">Full Story →</div></div>
      <div class="post"><div class="pic photo" role="img" aria-label="Photo of executives seated at a conference"><span class="tag">Onboarding</span></div>
        <h4>Why Halvern's New CFO Should Fail, But Won't</h4><p>By Martin Hale | On Jul 20, 2021</p><p>The critical difference between "inform" and "report" is timing. Informing happens before and reporting...</p><div class="more">Full Story →</div></div>
      <div class="book"><div class="cover" role="img" aria-label="Book cover of The First Quarter Playbook"></div><small>Browse All Of Our Books →</small></div>
    </div>
    <span class="btn">Read All Posts</span>
  </section>

  <section class="d-contact">
    <div class="band photo" role="img" aria-label="Dark photo of a meeting room"></div>
    <div class="eyebrow">Contact Us</div>
    <h3>Got Any Project You Would Like To Discuss?<br>Please Fill The Form Below:</h3>
    <div class="form"><div class="brand"><i class="brand-mark"></i>Bold Harbor</div>
      <div class="fields"><span>Name*</span><span>Email Address*</span><span>Phone Number*</span><span>Comment*</span></div>
      <span class="btn">Send Message</span></div>
    <div class="partners"><span>Northvale</span><span>Kestrel</span><span>Northvale</span><span>Northvale</span><span>Northvale</span></div>
    <div class="more">Click here to learn more about our clients →</div>
  </section>

  <section class="d-foot">
    <div class="col" style="left:75px;width:120px"><div class="brand"><i class="brand-mark"></i>Bold Harbor</div>
      <p style="margin-top:12px">Get done in 100 days what normally takes 6–12 months 95% of Bold Harbor clients succeed.</p>
      <div class="soc"><i></i><i></i><i></i></div></div>
    <div class="col" style="left:260px"><h5>Quick Links</h5><ul style="margin-top:10px"><li>Home</li><li>About Us</li><li>Books</li><li>Events</li><li>Resources</li></ul></div>
    <div class="col" style="left:408px"><h5>Contact Us</h5><p style="margin-top:10px;line-height:18px">☎ +1 555.010.4400<br>✉ boldharbor@email.com<br>⌖ Lorem Ipsum Street, USA</p></div>
  </section>
  <div class="d-copy">Copyright © 2021 Bold Harbor – All Rights Reserved</div>
</div>

</body>
</html>
```